Business Card- Can you make it cool vs boring!

Need a refresh on my business card! Want it to be modern but simple, classic and a pop of coolness! we do senior living and it is boring. but that doesn't mean our business card have to look boring! Open to two sided cards. our website is www.Bruvel-HQ.com

Target Market(s)

capital market

Industry/Entity Type

senior housing/ real estate

Contact Information for Business Card

logo/ name/ cell/ address/ www.Bruvel-HQ.com/ space for a QR code

Requirements
Must have
• maybe a QR code (do not make prominent I may not use the QR so design where it can be taken out) that link to more about us/ landing page. needs to be modern but clean
Should not have
• clip art or script

```html
<!DOCTYPE html>
<html lang="en">
<head>
<meta charset="utf-8">
<title>Bruvel Living – Business Card</title>
<link rel="stylesheet" href="https://fonts.googleapis.com/css2?family=Poppins:wght@400;500;600;700&display=swap">
<style>
  :root {
    --backdrop: #1f1f21;
    --rust: #ad5127;
    --paper: #ffffff;
    --ink-grey: #7a7a7a;
    --rule-grey: #9a9a9a;
    --logo-silver: #e6e6e6;
  }
  * { box-sizing: border-box; margin: 0; padding: 0; }
  html, body {
    width: 1200px; height: 1200px; overflow: hidden;
    background: var(--backdrop);
    font-family: "Poppins", sans-serif;
  }
  .canvas {
    position: relative; width: 1200px; height: 1200px;
    display: flex; flex-direction: column; align-items: center; justify-content: center;
    gap: 56px;
  }
  .card {
    position: relative; width: 880px; height: 503px;
    box-shadow: 0 18px 40px rgba(0,0,0,0.45);
    overflow: hidden;
  }
  /* Front side */
  .card--front {
    background: var(--rust);
    display: flex; align-items: center; justify-content: center;
  }
  .wordmark { display: flex; align-items: center; gap: 18px; }
  .wordmark__dot { width: 22px; height: 22px; border-radius: 50%; }
  .wordmark__name { font-weight: 500; line-height: 1; white-space: nowrap; }
  .card--front .wordmark__dot { background: var(--logo-silver); }
  .card--front .wordmark__name { color: var(--logo-silver); font-size: 64px; letter-spacing: 2px; }

  /* Back side */
  .card--back { background: var(--paper); }
  .card--back .wordmark { position: absolute; left: 58px; top: 178px; gap: 12px; }
  .card--back .wordmark__dot { background: var(--rust); width: 16px; height: 16px; }
  .card--back .wordmark__name { color: var(--rust); font-size: 40px; letter-spacing: 1px; }
  .divider {
    position: absolute; left: 440px; top: 120px; width: 2px; height: 210px;
    background: var(--rule-grey);
  }
  .contact { position: absolute; left: 488px; top: 110px; }
  .contact__name { color: var(--rust); font-weight: 700; font-size: 32px; line-height: 1.1; }
  .contact__role { color: var(--ink-grey); font-size: 16px; letter-spacing: 1px; margin-top: 2px; }
  .contact__rule { width: 70px; height: 3px; background: var(--rust); margin: 14px 0 18px; }
  .contact__list { list-style: none; display: flex; flex-direction: column; gap: 8px; }
  .contact__item { display: flex; align-items: center; gap: 12px; color: var(--ink-grey); font-size: 20px; letter-spacing: 0.5px; }
  .contact__icon { width: 24px; height: 24px; flex: none; }
  .address-band {
    position: absolute; left: 0; right: 0; top: 388px; height: 64px;
    background: var(--rust);
    display: flex; align-items: center; justify-content: center;
    color: var(--paper); font-weight: 500; font-size: 22px; letter-spacing: 1px;
  }
</style>
</head>
<body>
<main class="canvas">
  <section class="card card--front" aria-label="Card front">
    <div class="wordmark">
      <span class="wordmark__dot"></span>
      <span class="wordmark__name">Bruvel Living</span>
    </div>
  </section>

  <section class="card card--back" aria-label="Card back">
    <div class="wordmark">
      <span class="wordmark__dot"></span>
      <span class="wordmark__name">Bruvel Living</span>
    </div>
    <div class="divider"></div>
    <div class="contact">
      <p class="contact__name">Marcus R Hale</p>
      <p class="contact__role">CEO</p>
      <div class="contact__rule"></div>
      <ul class="contact__list">
        <li class="contact__item">
          <svg class="contact__icon" viewBox="0 0 24 24" aria-hidden="true">
            <circle cx="12" cy="12" r="12" fill="var(--rust)"/>
            <path d="M9 6.5c.6-.4 1.2-.2 1.5.4l.8 1.6c.3.6.1 1.1-.4 1.5l-.6.4c.4 1.4 1.4 2.8 2.6 3.6l.6-.4c.5-.4 1.1-.4 1.5.1l1.1 1.3c.4.5.4 1.1-.1 1.5-1.4 1.2-3.5.9-5.4-1.1-2-2-2.9-4.5-2.1-6.5.1-.3.3-.6.5-.8z" fill="#fff"/>
          </svg>
          <span>(512) 480-31275</span>
        </li>
        <li class="contact__item">
          <svg class="contact__icon" viewBox="0 0 24 24" aria-hidden="true">
            <circle cx="12" cy="12" r="12" fill="var(--rust)"/>
            <rect x="6" y="8" width="12" height="8.5" rx="1" fill="#fff"/>
            <path d="M6.5 8.5l5.5 4.2 5.5-4.2" fill="none" stroke="var(--rust)" stroke-width="1.2"/>
          </svg>
          <span>info@bruvelmail.com</span>
        </li>
        <li class="contact__item">
          <svg class="contact__icon" viewBox="0 0 24 24" aria-hidden="true">
            <circle cx="12" cy="12" r="12" fill="var(--rust)"/>
            <g fill="none" stroke="#fff" stroke-width="1.2">
              <circle cx="12" cy="12" r="6"/>
              <ellipse cx="12" cy="12" rx="2.6" ry="6"/>
              <path d="M6 12h12M7 9h10M7 15h10"/>
            </g>
          </svg>
          <span>www.Bruvel-HQ.com</span>
        </li>
      </ul>
    </div>
    <div class="address-band">4870 Cedar Mill Lane, Suite #650</div>
  </section>
</main>
</body>
</html>
```